Business card design needed

We need a business card design and possible logo for my new building construction business. I would like a masculine type of business design.

Thanks
Also can we please put my ABN number 47380926514 in as well thanks.
And use the colours black, orange and white. Cheers

Industry/Entity Type

Building

Contact Information for Business Card

Tarrow constructions, owner: Derek hollis, mobile:0417282613, email: hollo.d@quenmail.com, licence: 618374K

```html
<!DOCTYPE html>
<html lang="en">
<head>
<meta charset="utf-8">
<title>Tarrow constructions – Business Card</title>
<link href="https://fonts.googleapis.com/css2?family=Tinos:wght@400&display=swap" rel="stylesheet">
<style>
  :root {
    --ink: #160a03;
    --orange-light: #f7a23a;
    --orange: #ee7424;
    --orange-deep: #e0481c;
    --red-deep: #c8321a;
    --ring: #f08a2a;
    --ring-edge: #e2461c;
    --disc: #fbf7f4;
    --frame: #000000;
    --page: #ffffff;
  }
  * { box-sizing: border-box; margin: 0; padding: 0; }
  html, body {
    width: 1200px;
    height: 688px;
    overflow: hidden;
    background: var(--page);
  }
  .card {
    position: relative;
    width: 1200px;
    height: 688px;
    overflow: hidden;
    border: 3px solid var(--frame);
    font-family: "Tinos", "Times New Roman", serif;
    color: var(--ink);
  }
  .site-photo {
    position: absolute;
    inset: 0;
    background:
      radial-gradient(ellipse 55% 60% at 22% 30%, rgba(250, 190, 90, 0.85), rgba(250, 190, 90, 0) 70%),
      linear-gradient(115deg, var(--orange-light) 0%, var(--orange) 40%, var(--orange-deep) 72%, var(--red-deep) 100%);
  }
  .owner-name {
    position: absolute;
    left: 84px;
    top: 44px;
    font-size: 53px;
    line-height: 1;
    font-weight: 400;
  }
  .owner-role {
    position: absolute;
    left: 298px;
    top: 116px;
    font-size: 35px;
    line-height: 1;
  }
  .contact {
    position: absolute;
    left: 32px;
    font-size: 42px;
    line-height: 1;
    white-space: pre;
  }
  .contact--mobile { top: 418px; }
  .contact--licence { top: 472px; }
  .contact--abn { top: 526px; }
  .contact--email { top: 592px; font-size: 38px; }
  .brand-mark {
    position: absolute;
    left: 613px;
    top: 103px;
    width: 528px;
    height: 528px;
  }
  .brand-name {
    position: absolute;
    left: 613px;
    top: 103px;
    width: 528px;
    height: 528px;
    display: flex;
    flex-direction: column;
    align-items: center;
    justify-content: center;
    font-size: 62px;
    line-height: 1.15;
    color: var(--ink);
    text-align: center;
  }
</style>
</head>
<body>
  <div class="card">
    <div class="site-photo" role="img" aria-label="Photograph of two builders in hard hats reviewing plans on a timber-framed construction site, tinted orange"></div>

    <h1 class="owner-name">Derek Hollis</h1>
    <p class="owner-role">proprietor</p>

    <p class="contact contact--mobile">Mobile  #  0417282613</p>
    <p class="contact contact--licence">Licence #  618374 K</p>
    <p class="contact contact--abn">ABN      #  47380926514</p>
    <p class="contact contact--email">Email- hollo.d@quenmail.com</p>

    <svg class="brand-mark" viewBox="0 0 528 528" aria-hidden="true">
      <circle cx="264" cy="264" r="252" fill="var(--disc)" stroke="var(--ring)" stroke-width="20"/>
      <circle cx="264" cy="264" r="262" fill="none" stroke="var(--ring-edge)" stroke-width="3"/>
    </svg>
    <p class="brand-name"><span>Tarrow</span><span>constructions</span></p>
  </div>
</body>
</html>
```